Bref créative
Business Cards, Letterhead, Envelopes, Fax Cover, Email Signature, Truck
Brindle Roofing Ltd.
I need double sided standard sized Business Card [3.5" x 2"]
Do not limit yourself to font used in logo
Professional
Tomasz Oduya
42 Fairwick Lane NE
Calgary AB T3M2R8
tomi@brindleroofing.example
www.brindleroofing.example
Open to different ideas. For example : just logo, web address etc
Photograph-1 of truck
Picture 2
Picture-3
Picture-4
Picture-5
Color scheme(s)to be used for Truck

```html
<!DOCTYPE html>
<html lang="en">
<head>
<meta charset="utf-8">
<title>Brindle Roofing Ltd. – Business Card</title>
<link href="https://fonts.googleapis.com/css2?family=Didact+Gothic&display=swap" rel="stylesheet">
<style>
  :root {
    --backdrop: #1c1c1c;
    --card: #ffffff;
    --green-dark: #4f6b2c;
    --green: #7a9a4a;
    --green-light: #a9c27a;
    --ink: #5a5a5a;
    --ink-soft: #8a8a8a;
    --rule: #b9b9b9;
  }
  html, body {
    margin: 0;
    padding: 0;
    width: 1200px;
    height: 901px;
    overflow: hidden;
    background: var(--backdrop);
    font-family: "Didact Gothic", "Century Gothic", sans-serif;
  }
  .stage {
    position: relative;
    width: 1200px;
    height: 901px;
  }
  .card {
    position: absolute;
    top: 324px;
    width: 431px;
    height: 255px;
    background: var(--card);
    border-radius: 14px;
    overflow: hidden;
  }
  .card--front { left: 153px; }
  .card--back { left: 616px; }
  .card__band {
    position: absolute;
    top: 0;
    height: 100%;
    width: 70px;
  }
  .card--front .card__band { left: 0; }
  .card--back .card__band { right: 0; }

  .brand {
    position: absolute;
    left: 70px;
    top: 58px;
    display: flex;
    align-items: center;
    gap: 10px;
  }
  .brand__dot {
    width: 26px;
    height: 26px;
    border-radius: 50%;
    background: var(--green);
  }
  .brand__name {
    font-size: 30px;
    color: var(--green-dark);
    letter-spacing: -0.5px;
    white-space: nowrap;
  }
  .holder {
    position: absolute;
    left: 84px;
    top: 133px;
    font-size: 13px;
    font-weight: 700;
    color: var(--green-dark);
    letter-spacing: 0.3px;
  }
  .divider {
    position: absolute;
    left: 238px;
    top: 128px;
    width: 1px;
    height: 96px;
    background: var(--rule);
  }
  .contact {
    position: absolute;
    left: 250px;
    top: 127px;
    margin: 0;
    padding: 0;
    list-style: none;
    font-size: 9px;
    line-height: 12.5px;
    color: var(--ink);
  }
  .contact__row {
    display: flex;
    align-items: center;
    gap: 5px;
  }
  .contact__row--gap { margin-top: 8px; }
  .contact__icon {
    width: 7px;
    height: 7px;
    flex: none;
  }
  .contact__spacer { width: 7px; flex: none; }

  .web {
    position: absolute;
    left: 90px;
    top: 150px;
    font-size: 20px;
    color: var(--ink-soft);
    letter-spacing: 0.2px;
  }
  .web__domain { color: var(--green-dark); }
</style>
</head>
<body>
<main class="stage">

  <section class="card card--front" aria-label="Business card front">
    <svg class="card__band" viewBox="0 0 70 255" preserveAspectRatio="none" aria-hidden="true">
      <defs>
        <linearGradient id="band-front" x1="0" y1="0" x2="1" y2="0">
          <stop offset="0" stop-color="#5d7a34"/>
          <stop offset="0.7" stop-color="#8fae5c"/>
          <stop offset="1" stop-color="#b8cf8e"/>
        </linearGradient>
      </defs>
      <path d="M0 0 H52 C22 60 22 195 52 255 H0 Z" fill="url(#band-front)"/>
    </svg>

    <div class="brand">
      <span class="brand__dot"></span>
      <span class="brand__name">Brindle Roofing Ltd.</span>
    </div>

    <div class="holder">Tomasz Oduya</div>
    <div class="divider"></div>

    <ul class="contact">
      <li class="contact__row"><span class="contact__spacer"></span>42 Fairwick Lane NE</li>
      <li class="contact__row"><span class="contact__spacer"></span>Calgary AB T3M2R8</li>
      <li class="contact__row contact__row--gap">
        <svg class="contact__icon" viewBox="0 0 10 10" aria-label="Phone"><rect x="2.5" y="0.5" width="5" height="9" rx="1" fill="none" stroke="#5a5a5a"/></svg>403 555 0142</li>
      <li class="contact__row">
        <svg class="contact__icon" viewBox="0 0 10 10" aria-label="Mobile"><rect x="2.5" y="0.5" width="5" height="9" rx="1" fill="#5a5a5a"/></svg>403 555 0187</li>
      <li class="contact__row">
        <svg class="contact__icon" viewBox="0 0 10 10" aria-label="Fax"><rect x="0.5" y="3" width="9" height="6" fill="none" stroke="#5a5a5a"/><rect x="2.5" y="0.5" width="5" height="3" fill="#5a5a5a"/></svg>403 555 0199</li>
      <li class="contact__row contact__row--gap">
        <svg class="contact__icon" viewBox="0 0 10 10" aria-label="Email"><rect x="0.5" y="2" width="9" height="6" fill="none" stroke="#5a5a5a"/><path d="M0.5 2 L5 5.5 L9.5 2" fill="none" stroke="#5a5a5a"/></svg>tomi@brindleroofing.example</li>
      <li class="contact__row">
        <svg class="contact__icon" viewBox="0 0 10 10" aria-label="Website"><circle cx="5" cy="5" r="4.3" fill="none" stroke="#5a5a5a"/><path d="M0.7 5 H9.3 M5 0.7 V9.3" stroke="#5a5a5a"/></svg>www.brindleroofing.example</li>
    </ul>
  </section>

  <section class="card card--back" aria-label="Business card back">
    <svg class="card__band" viewBox="0 0 70 255" preserveAspectRatio="none" aria-hidden="true">
      <defs>
        <linearGradient id="band-back" x1="1" y1="0" x2="0" y2="0">
          <stop offset="0" stop-color="#5d7a34"/>
          <stop offset="0.7" stop-color="#8fae5c"/>
          <stop offset="1" stop-color="#b8cf8e"/>
        </linearGradient>
      </defs>
      <path d="M70 0 H18 C48 60 48 195 18 255 H70 Z" fill="url(#band-back)"/>
    </svg>

    <div class="web">www.<span class="web__domain">brindleroofing</span>.example</div>
  </section>

</main>
</body>
</html>
```